looking to have a web site for the company which provides services in the industrial and commercial sectors such as: electrical, automation control and system integration, construction and maintenance, millwright, equipment assembly repair and installation. I have the domain already brovinacorp.net and logo. Most recent projects fulfilled for the following clients: MeadowlarkFeeds, Calderwick University, ORIN, TALVIK, Ostmar, Northfield Grains

Target Market(s)

industrial and commercial sectors in electrical, automation, millwright and fabrication fields

Industry/Entity Type

Industrial

Coding

Coded - Design and coding required

Number of Pages Required

5+ page

Font styles to use
Sans Serif

Colors

Designer to choose colors to be used in the design.

Requirements
Nice to have
• looking to get something not complicated, nicely presented with minimum or no scrolling

```html
<!DOCTYPE html>
<html lang="en">
<head>
<meta charset="utf-8">
<title>Brovina Corp — Industrial &amp; Commercial Services</title>
<link href="https://fonts.googleapis.com/css2?family=Lato:ital,wght@0,400;0,700;0,900;1,900&family=Open+Sans:wght@400;600;700&display=swap" rel="stylesheet">
<style>
:root{
  --blue:#1b7bc4;
  --blue-dark:#13609c;
  --blue-deep:#0f4f86;
  --ink:#222;
  --text:#444;
  --muted:#777;
  --light:#efefef;
  --line:#ddd;
  --topbar:#2b2b2b;
  --footer:#3a3a3a;
  --bottom:#232323;
  --white:#fff;
}
*{box-sizing:border-box;margin:0;padding:0}
html,body{width:1200px;height:4534px;overflow:hidden}
body{font-family:"Open Sans",Arial,sans-serif;color:var(--text);background:var(--white);position:relative;font-size:15px}
a{color:inherit;text-decoration:none}

/* top bar */
.topbar{position:absolute;left:0;top:0;width:1200px;height:36px;background:var(--topbar);color:#ddd;font-size:14px}
.topbar .phone{position:absolute;left:120px;top:9px;display:flex;gap:8px;align-items:center}
.topbar .mail{position:absolute;left:540px;top:9px;display:flex;gap:8px;align-items:center}
.topbar .social{position:absolute;right:118px;top:8px;display:flex;gap:6px}
.dot-icon{width:20px;height:20px;border-radius:50%;background:#ddd}

/* header */
.header{position:absolute;left:0;top:36px;width:1200px;height:104px;display:flex;align-items:center;justify-content:center}
.brand{text-align:center;font-family:Lato,sans-serif;color:var(--blue-deep)}
.brand .name{font-size:46px;font-weight:900;letter-spacing:2px;line-height:1}
.brand .sub{font-size:14px;font-weight:700;letter-spacing:8px;margin-top:2px;color:#666}

/* nav */
.nav{position:absolute;left:0;top:140px;width:1200px;height:54px;background:var(--blue)}
.nav ul{list-style:none;position:absolute;left:120px;top:0;height:54px;display:flex}
.nav li{height:54px;padding:0 18px;display:flex;align-items:center;color:#fff;font-family:Lato,sans-serif;font-weight:700;font-size:14px;letter-spacing:.5px}
.nav li.active{background:var(--blue-dark)}
.nav .search{position:absolute;left:872px;top:16px}
.nav .quote{position:absolute;left:948px;top:12px;height:30px;padding:0 14px;border:2px solid #fff;color:#fff;font:700 14px Lato,sans-serif;display:flex;align-items:center}

/* hero */
.hero{position:absolute;left:0;top:194px;width:1200px;height:652px;background:linear-gradient(100deg,#6f6f6c 0%,#9a9a96 25%,#b9bcbf 50%,#8c8b84 70%,#5d6650 100%)}
.hero-caption{position:absolute;left:357px;top:266px;width:520px;height:190px;background:rgba(40,40,40,.55);text-align:center;padding-top:48px;color:#fff}
.hero-caption h1{font:italic 900 30px Lato,sans-serif;letter-spacing:.5px}
.hero-caption p{font-size:15px;font-weight:600;line-height:20px;margin-top:6px}
.btn{display:inline-flex;align-items:center;gap:10px;background:var(--blue);color:#fff;font:700 14px "Open Sans",sans-serif;height:36px;padding:0 6px 0 18px}
.btn .arr{width:22px;height:22px;border:1.5px solid #fff;border-radius:50%;display:flex;align-items:center;justify-content:center}
.hero-caption .btn{margin-top:14px}
.hero .slide-arrow{position:absolute;top:294px;width:40px;height:40px;background:rgba(255,255,255,.7);display:flex;align-items:center;justify-content:center}
.hero .dots{position:absolute;left:552px;top:570px;display:flex;gap:12px}
.hero .dots span{width:14px;height:14px;border-radius:50%;background:#aab;opacity:.8}
.hero .dots span.on{background:var(--blue);opacity:1}

/* section heads */
.sec-title{position:absolute;left:0;width:1200px;text-align:center;font:900 30px Lato,sans-serif;color:var(--ink);letter-spacing:.5px}
.sec-title::after{content:"";display:block;width:60px;height:4px;background:var(--blue);margin:6px auto 0}
.sec-sub{position:absolute;left:0;width:1200px;text-align:center;font-size:15px;color:var(--text)}

/* services */
.service{position:absolute;width:248px;height:220px;padding:28px 0 0 0}
.service .icon{height:56px}
.service h3{font:900 16px Lato,sans-serif;color:var(--ink);margin-top:10px;line-height:19px;text-transform:uppercase;min-height:38px;display:flex;align-items:center}
.service p{font-size:14px;line-height:19px;margin-top:6px}
.service .more{display:flex;align-items:center;gap:8px;font-weight:700;font-size:14px;color:var(--ink);margin-top:12px}
.service .more .arr{width:20px;height:20px;border:1.5px solid var(--ink);border-radius:50%;display:flex;align-items:center;justify-content:center}
.service.featured{background:var(--blue);color:#fff;padding-left:30px}
.service.featured h3,.service.featured .more{color:#fff}
.service.featured .more .arr{border-color:#fff}

/* who we are */
.about{position:absolute;left:0;top:1536px;width:1200px;height:701px;background:linear-gradient(90deg,#f4f4f4,#e8e8e8)}
.about h2{position:absolute;left:121px;top:100px;font:900 30px Lato,sans-serif;color:var(--ink)}
.about h2::after{content:"";display:block;width:60px;height:4px;background:var(--blue);margin-top:6px}
.about .copy{position:absolute;left:121px;top:158px;width:440px;font-size:14.5px;line-height:19px}
.about .copy p+p{margin-top:12px}
.timeline{position:absolute;left:121px;top:408px;width:400px}
.timeline .rail{position:absolute;left:12px;top:12px;width:300px;height:2px;background:#aaa}
.timeline .step{position:absolute;top:0;width:120px;font-size:14px;line-height:17px}
.timeline .step .tick{width:26px;height:26px;border-radius:50%;border:2px solid var(--blue);background:#fff;display:flex;align-items:center;justify-content:center;margin-bottom:8px}
.about .btn{position:absolute;left:121px;top:550px}
.ph{position:absolute}

/* projects */
.filters{position:absolute;left:0;top:2358px;width:1200px;display:flex;justify-content:center;gap:26px;font:700 13px Lato,sans-serif;color:var(--ink)}
.filters .on{color:var(--blue)}
.project{position:absolute;width:306px}
.project .img{height:192px}
.project p{font-size:13.5px;line-height:17px;margin-top:10px;color:var(--ink)}

/* stats */
.stats{position:absolute;left:0;top:3047px;width:1200px;height:293px;background:linear-gradient(90deg,rgba(27,123,196,.92),rgba(22,108,178,.9)),linear-gradient(120deg,#4c6a85,#8aa0b4,#3d5870)}
.stat{position:absolute;top:112px;width:240px;text-align:center;color:#fff}
.stat .num{font:900 56px Lato,sans-serif;line-height:56px}
.stat .label{font:900 18px Lato,sans-serif;margin-top:8px;text-transform:uppercase}
.stat .since{font:700 14px Lato,sans-serif}

/* blog */
.post{position:absolute;top:3530px;width:472px}
.post .img{height:240px;position:relative}
.post .tag{position:absolute;left:0;bottom:0;width:100%;height:40px;background:rgba(27,123,196,.85);color:#fff;font:900 18px Lato,sans-serif;padding-left:22px;display:flex;align-items:center}
.post .meta{display:flex;gap:40px;font-size:14px;margin-top:24px;padding-left:22px}
.post .meta span{display:flex;align-items:center;gap:8px}
.post p{font-size:14.5px;line-height:19px;margin-top:18px;padding-left:22px;padding-right:10px;color:var(--ink)}
.post .more{display:flex;align-items:center;gap:8px;font-weight:700;font-size:14px;color:var(--ink);margin-top:16px;padding-left:22px}
.post .more .arr{width:20px;height:20px;border:1.5px solid var(--ink);border-radius:50%;display:flex;align-items:center;justify-content:center}

/* clients */
.clients{position:absolute;left:0;top:3945px;width:1200px;height:212px;background:var(--light)}
.client{position:absolute;top:75px;width:234px;height:97px;background:#fff;display:flex;align-items:center;justify-content:center;gap:10px;font:900 26px Lato,sans-serif;color:var(--ink)}
.client .mark{width:22px;height:22px;border-radius:50%;background:var(--blue)}
.clients .arrow{position:absolute;top:102px;width:36px;height:44px;background:#ccc;display:flex;align-items:center;justify-content:center}

/* footer */
.footer{position:absolute;left:0;top:4157px;width:1200px;height:338px;background:var(--footer);color:#e6e6e6}
.footer h4{font:900 16px Lato,sans-serif;color:#fff;text-transform:uppercase}
.footer h4::after{content:"";display:block;width:40px;height:3px;background:var(--blue);margin-top:6px}
.footer .col{position:absolute;top:86px;font-size:14px;line-height:20px}
.footer .brand{text-align:left;color:#fff}
.footer .brand .sub{color:#ccc}
.footer ul{list-style:none;margin-top:14px}
.footer li::before{content:"> ";}
.footer .signup{display:flex;margin-top:16px}
.footer .signup span{width:200px;height:34px;background:#fff;color:#999;font-size:12px;padding-left:10px;display:flex;align-items:center}
.footer .signup b{width:36px;height:34px;background:var(--blue);display:flex;align-items:center;justify-content:center}
.bottombar{position:absolute;left:0;top:4495px;width:1200px;height:39px;background:var(--bottom);color:#ddd;font-size:13px;font-weight:600}
.bottombar .copy{position:absolute;left:121px;top:11px}
.bottombar .social{position:absolute;right:118px;top:8px;display:flex;gap:8px}
</style>
</head>
<body>

<div class="topbar">
  <div class="phone"><svg width="14" height="14" viewBox="0 0 24 24"><path d="M6.6 10.8a15 15 0 006.6 6.6l2.2-2.2c.3-.3.7-.4 1-.2 1.1.4 2.3.6 3.6.6.6 0 1 .4 1 1V20c0 .6-.4 1-1 1A17 17 0 013 4c0-.6.4-1 1-1h3.5c.6 0 1 .4 1 1 0 1.2.2 2.4.6 3.6.1.3 0 .7-.2 1z" fill="#ddd"/></svg>123-4567-8910</div>
  <div class="mail"><svg width="16" height="12" viewBox="0 0 16 12"><rect x=".5" y=".5" width="15" height="11" fill="none" stroke="#ddd"/><path d="M.5.5l7.5 6 7.5-6" fill="none" stroke="#ddd"/></svg>info@brovinacorp.net</div>
  <div class="social"><span class="dot-icon"></span><span class="dot-icon"></span><span class="dot-icon"></span><span class="dot-icon"></span><span class="dot-icon"></span></div>
</div>

<header class="header">
  <div class="brand"><div class="name">BROVINA</div><div class="sub">CORP</div></div>
</header>

<nav class="nav">
  <ul>
    <li class="active">HOME</li><li>ABOUT US</li><li>SERVICES</li><li>PROJECT</li><li>CLIENTS</li><li>BLOG</li><li>CONTACT</li>
  </ul>
  <svg class="search" width="22" height="22" viewBox="0 0 22 22"><circle cx="9" cy="9" r="7" fill="none" stroke="#fff" stroke-width="2.5"/><path d="M14 14l6 6" stroke="#fff" stroke-width="3"/></svg>
  <div class="quote">GET A QUOTE</div>
</nav>

<section class="hero" role="img" aria-label="Grain silos and an industrial elevator tower under a cloudy sky">
  <div class="slide-arrow" style="left:0"><svg width="14" height="20"><path d="M12 2L3 10l9 8" fill="#888"/></svg></div>
  <div class="slide-arrow" style="right:0"><svg width="14" height="20"><path d="M2 2l9 8-9 8" fill="#888"/></svg></div>
  <div class="hero-caption">
    <h1>LOREM IPSUM IS SIMPLY DUMMY</h1>
    <p>Lorem Ipsum is simply dummy text of the printing and industry.<br>Lorem Ipsum has been the industry's</p>
    <a class="btn">Read More <span class="arr"><svg width="10" height="10"><path d="M1 5h7M5 2l3 3-3 3" stroke="#fff" fill="none" stroke-width="1.5"/></svg></span></a>
  </div>
  <div class="dots"><span class="on"></span><span></span><span></span><span></span></div>
</section>

<h2 class="sec-title" style="top:900px">OUR SERVICES</h2>
<p class="sec-sub" style="top:952px">What we can do for you</p>

<div class="service" style="left:121px;top:1013px">
  <div class="icon"><svg width="50" height="50" viewBox="0 0 50 50"><circle cx="25" cy="25" r="22" fill="none" stroke="var(--blue)" stroke-width="3"/><path d="M28 8L15 28h9l-3 14 14-21h-9z" fill="var(--blue)"/></svg></div>
  <h3>Electrical</h3><p>Lorem Ipsum is simply dumy of the printing and industry.</p>
  <a class="more">Read More.. <span class="arr"><svg width="10" height="10"><path d="M1 5h7M5 2l3 3-3 3" stroke="#222" fill="none" stroke-width="1.5"/></svg></span></a>
</div>
<div class="service featured" style="left:350px;top:1013px">
  <div class="icon"><svg width="54" height="54" viewBox="0 0 54 54"><circle cx="27" cy="27" r="13" fill="none" stroke="#fff" stroke-width="8" stroke-dasharray="6 4"/><circle cx="27" cy="27" r="9" fill="none" stroke="#fff" stroke-width="3"/></svg></div>
  <h3>Automation<br>Control</h3><p>Lorem Ipsum is simply dumy of the printing and industry.</p>
  <a class="more">Read More.. <span class="arr"><svg width="10" height="10"><path d="M1 5h7M5 2l3 3-3 3" stroke="#fff" fill="none" stroke-width="1.5"/></svg></span></a>
</div>
<div class="service" style="left:650px;top:1013px">
  <div class="icon"><svg width="60" height="50" viewBox="0 0 60 50"><rect x="4" y="14" width="52" height="22" rx="11" fill="none" stroke="var(--blue)" stroke-width="3"/><path d="M18 25h24M36 19l6 6-6 6M24 19l-6 6 6 6" stroke="var(--blue)" stroke-width="3" fill="none"/></svg></div>
  <h3>System<br>Integration,</h3><p>Lorem Ipsum is simply dumy of the printing and industry.</p>
  <a class="more">Read More.. <span class="arr"><svg width="10" height="10"><path d="M1 5h7M5 2l3 3-3 3" stroke="#222" fill="none" stroke-width="1.5"/></svg></span></a>
</div>
<div class="service" style="left:895px;top:1013px">
  <div class="icon"><svg width="60" height="50" viewBox="0 0 60 50"><path d="M6 46h48M14 46V14h6v32M14 14l30-8M20 14l26 8M46 14v14" stroke="var(--blue)" stroke-width="3" fill="none"/><rect x="40" y="28" width="12" height="8" fill="var(--blue)"/><rect x="8" y="38" width="18" height="8" fill="var(--blue)"/></svg></div>
  <h3>Construction</h3><p>Lorem Ipsum is simply dumy of the printing and industry.</p>
  <a class="more">Read More.. <span class="arr"><svg width="10" height="10"><path d="M1 5h7M5 2l3 3-3 3" stroke="#222" fill="none" stroke-width="1.5"/></svg></span></a>
</div>

<div class="service" style="left:121px;top:1255px">
  <div class="icon"><svg width="54" height="54" viewBox="0 0 54 54"><circle cx="27" cy="27" r="14" fill="none" stroke="var(--blue)" stroke-width="9" stroke-dasharray="6 4"/><circle cx="27" cy="27" r="6" fill="var(--blue)"/></svg></div>
  <h3>Maintenance</h3><p>Lorem Ipsum is simply dumy of the printing and industry.</p>
  <a class="more">Read More.. <span class="arr"><svg width="10" height="10"><path d="M1 5h7M5 2l3 3-3 3" stroke="#222" fill="none" stroke-width="1.5"/></svg></span></a>
</div>
<div class="service" style="left:390px;top:1255px">
  <div class="icon"><svg width="64" height="50" viewBox="0 0 64 50"><path d="M4 26h40" stroke="var(--blue)" stroke-width="7"/><path d="M44 16h10v6h-6v8h6v6H44z" fill="var(--blue)"/><path d="M10 18v16M18 18v16M26 18v16" stroke="#fff" stroke-width="1.5"/></svg></div>
  <h3>Millwright</h3><p>Lorem Ipsum is simply dumy of the printing and industry.</p>
  <a class="more">Read More.. <span class="arr"><svg width="10" height="10"><path d="M1 5h7M5 2l3 3-3 3" stroke="#222" fill="none" stroke-width="1.5"/></svg></span></a>
</div>
<div class="service" style="left:650px;top:1255px">
  <div class="icon"><svg width="54" height="54" viewBox="0 0 54 54"><path d="M10 44L36 18" stroke="var(--blue)" stroke-width="6"/><circle cx="40" cy="14" r="8" fill="none" stroke="var(--blue)" stroke-width="5"/><path d="M12 10l30 32" stroke="var(--blue)" stroke-width="5"/><rect x="6" y="4" width="10" height="10" fill="var(--blue)"/></svg></div>
  <h3>Equipment<br>Assembly Repair</h3><p>Lorem Ipsum is simply dumy of the printing and industry.</p>
  <a class="more">Read More.. <span class="arr"><svg width="10" height="10"><path d="M1 5h7M5 2l3 3-3 3" stroke="#222" fill="none" stroke-width="1.5"/></svg></span></a>
</div>
<div class="service" style="left:895px;top:1255px">
  <div class="icon"><svg width="60" height="50" viewBox="0 0 60 50"><rect x="6" y="6" width="48" height="30" fill="none" stroke="var(--blue)" stroke-width="3"/><path d="M12 30l10-10 8 6 10-12 8 8" stroke="var(--blue)" stroke-width="3" fill="none"/><path d="M2 42h56" stroke="var(--blue)" stroke-width="4"/></svg></div>
  <h3>Installation</h3><p>Lorem Ipsum is simply dumy of the printing and industry.</p>
  <a class="more">Read More.. <span class="arr"><svg width="10" height="10"><path d="M1 5h7M5 2l3 3-3 3" stroke="#222" fill="none" stroke-width="1.5"/></svg></span></a>
</div>

<section class="about">
  <h2>WHO WE ARE</h2>
  <div class="copy">
    <p>Lorem Ipsum is simply dummy text of the printing and typesetting industry. Lorem Ipsum has been the industry's standard dummy text ever since the 1500s,</p>
    <p>when an unknown printer took a galley of type and scrambled it to make a type specimen book. It has survived not only five centuries, but also the leap into electronic typesetting, remaining essentially unchanged. It was popularised in the 1960s with the release of Pressline sheets containing Lorem Ipsum passages, and more recently with desktop publishing software like Folio Layout including versions of Lorem Ipsum</p>
  </div>
  <div class="timeline">
    <div class="rail"></div>
    <div class="step" style="left:0"><div class="tick"><svg width="12" height="10"><path d="M1 5l3 3 7-7" stroke="var(--blue)" stroke-width="2" fill="none"/></svg></div>We Are<br>Passionate</div>
    <div class="step" style="left:165px"><div class="tick"><svg width="12" height="10"><path d="M1 5l3 3 7-7" stroke="var(--blue)" stroke-width="2" fill="none"/></svg></div>Honest<br>Depensable</div>
    <div class="step" style="left:318px"><div class="tick"><svg width="12" height="10"><path d="M1 5l3 3 7-7" stroke="var(--blue)" stroke-width="2" fill="none"/></svg></div>Always<br>Improving</div>
  </div>
  <a class="btn">Read More <span class="arr"><svg width="10" height="10"><path d="M1 5h7M5 2l3 3-3 3" stroke="#fff" fill="none" stroke-width="1.5"/></svg></span></a>
  <div class="ph" style="left:635px;top:96px;width:217px;height:212px;background:linear-gradient(160deg,#a7aeb5,#6f6a63)" role="img" aria-label="Grain silos with a red-roofed storage tank"></div>
  <div class="ph" style="left:635px;top:314px;width:217px;height:266px;background:linear-gradient(160deg,#4d4a45,#8c7f6e)" role="img" aria-label="Interior of a plant room with industrial machinery"></div>
  <div class="ph" style="left:862px;top:202px;width:220px;height:408px;background:linear-gradient(180deg,#a9b3bd 0%,#8c9093 50%,#5d7248 100%)" role="img" aria-label="Silo exterior beside a green field"></div>
</section>

<h2 class="sec-title" style="top:2291px">OUR LATEST PROJECT</h2>
<div class="filters"><span class="on">ALL</span><span>ELECTRICAL</span><span>AUTOMATION CONTROL</span><span>SYSTEM INTEGRATION</span><span>CONSTRUCTION</span></div>

<div class="project" style="left:121px;top:2403px"><div class="img" style="background:linear-gradient(135deg,#6f7880,#b0443c 50%,#5b6670)" role="img" aria-label="Electrical panel with red breakers and wiring"></div><p>Lorem Ipsum is simply dummy text of the printing</p></div>
<div class="project" style="left:447px;top:2403px"><div class="img" style="background:linear-gradient(135deg,#5a524a,#8e8577 50%,#3f3a35)" role="img" aria-label="Industrial conveyor machinery"></div><p>Lorem Ipsum is simply dummy text of the printing</p></div>
<div class="project" style="left:776px;top:2403px"><div class="img" style="background:linear-gradient(135deg,#8a8580,#b8b4ae 50%,#57524c)" role="img" aria-label="Control cabinets in a plant room"></div><p>Lorem Ipsum is simply dummy text of the printing</p></div>
<div class="project" style="left:121px;top:2675px"><div class="img" style="background:linear-gradient(135deg,#6c645a,#a69c8d 50%,#48433d)" role="img" aria-label="Steel piping and structural frames"></div><p>Lorem Ipsum is simply dummy text of the printing</p></div>
<div class="project" style="left:447px;top:2675px"><div class="img" style="background:linear-gradient(135deg,#7a7068,#b1a393 50%,#4c4640)" role="img" aria-label="Processing equipment with ducts"></div><p>Lorem Ipsum is simply dummy text of the printing</p></div>
<div class="project" style="left:776px;top:2675px"><div class="img" style="background:linear-gradient(135deg,#5e5852,#a9a49c 50%,#6f6860)" role="img" aria-label="Stainless steel tanks and valves"></div><p>Lorem Ipsum is simply dummy text of the printing</p></div>

<a class="btn" style="position:absolute;left:538px;top:2945px">View More <span class="arr"><svg width="10" height="10"><path d="M1 5h7M5 2l3 3-3 3" stroke="#fff" fill="none" stroke-width="1.5"/></svg></span></a>

<section class="stats" role="img" aria-label="Blue-tinted band over a photo of factory machinery">
  <div class="stat" style="left:75px"><div class="num">5502</div><div class="label">Project Done</div><div class="since">In Past 5 year</div></div>
  <div class="stat" style="left:342px"><div class="num">6805</div><div class="label">Problem Solved</div><div class="since">Since 2012</div></div>
  <div class="stat" style="left:626px"><div class="num">805</div><div class="label">Development</div><div class="since">Since 2012</div></div>
  <div class="stat" style="left:900px"><div class="num">2005</div><div class="label">Client Handle</div><div class="since">Over All time</div></div>
</section>

<h2 class="sec-title" style="top:3433px">LATEST BLOG POST</h2>
<p class="sec-sub" style="top:3486px">Check the latest news from our blog</p>

<article class="post" style="left:121px">
  <div class="img" style="background:linear-gradient(135deg,#8d8d8d,#3e3e3e 50%,#a0a0a0)" role="img" aria-label="Black and white photo of plant structures"><div class="tag">ELECTRICAL</div></div>
  <div class="meta"><span><svg width="14" height="14"><rect x="1" y="2" width="12" height="11" fill="none" stroke="var(--blue)" stroke-width="1.5"/><path d="M1 5h12" stroke="var(--blue)" stroke-width="1.5"/></svg>11th October,2017</span><span><svg width="14" height="14"><circle cx="7" cy="4" r="3" fill="var(--blue)"/><path d="M1 14a6 6 0 0112 0z" fill="var(--blue)"/></svg>Dana Holt</span></div>
  <p>Lorem Ipsum is simply dummy text of the printing and typesetting industry. Lorem Ipsum has been the industry's standard dummy text ever since the 1500s.</p>
  <a class="more">Read More.. <span class="arr"><svg width="10" height="10"><path d="M1 5h7M5 2l3 3-3 3" stroke="#222" fill="none" stroke-width="1.5"/></svg></span></a>
</article>
<article class="post" style="left:611px">
  <div class="img" style="background:linear-gradient(135deg,#6f6a64,#b6a996 50%,#4e5a52)" role="img" aria-label="Wired control panel with green terminals"><div class="tag">SYSTEM &nbsp;INTEGRATION</div></div>
  <div class="meta"><span><svg width="14" height="14"><rect x="1" y="2" width="12" height="11" fill="none" stroke="var(--blue)" stroke-width="1.5"/><path d="M1 5h12" stroke="var(--blue)" stroke-width="1.5"/></svg>11th October,2017</span><span><svg width="14" height="14"><circle cx="7" cy="4" r="3" fill="var(--blue)"/><path d="M1 14a6 6 0 0112 0z" fill="var(--blue)"/></svg>Dana Holt</span></div>
  <p>Lorem Ipsum is simply dummy text of the printing and typesetting industry. Lorem Ipsum has been the industry's standard dummy text ever since the 1500s.</p>
  <a class="more">Read More.. <span class="arr"><svg width="10" height="10"><path d="M1 5h7M5 2l3 3-3 3" stroke="#222" fill="none" stroke-width="1.5"/></svg></span></a>
</article>

<section class="clients">
  <h2 class="sec-title" style="top:22px;font-size:28px">OUR CLIENTS</h2>
  <div class="arrow" style="left:0"><svg width="12" height="18"><path d="M10 2L3 9l7 7" fill="#fff"/></svg></div>
  <div class="arrow" style="right:0"><svg width="12" height="18"><path d="M2 2l7 7-7 7" fill="#fff"/></svg></div>
  <div class="client" style="left:115px;font-size:22px"><span class="mark"></span>MeadowlarkFeeds</div>
  <div class="client" style="left:363px"><span class="mark"></span>ORIN</div>
  <div class="client" style="left:608px"><span class="mark"></span>TALVIK</div>
  <div class="client" style="left:835px"><span class="mark"></span>Ostmar</div>
</section>

<footer class="footer">
  <div class="col" style="left:121px;top:76px;width:260px">
    <div class="brand"><div class="name" style="font-size:38px">BROVINA</div><div class="sub">CORP</div></div>
    <p style="margin-top:22px;font-weight:600">Lorem Ipsum is simply dummy text of the printing and typesetting industry. Lorem Ipsum has been the industry's standard dummy text ever since the 1500s.</p>
  </div>
  <div class="col" style="left:423px"><h4>About Us</h4>
    <ul><li>Home</li><li>About us</li><li>Services</li><li>Project</li><li>Clients</li><li>Blog</li></ul>
  </div>
  <div class="col" style="left:605px"><h4>Contact Us</h4>
    <p style="margin-top:14px;font-weight:600">12345 West 23th Street,<br>Suite 120, Canada</p>
    <p style="margin-top:6px">Phone: 123 456 7890<br>Fax: 123 456 7890<br>info@brovinacorp.net</p>
  </div>
  <div class="col" style="left:855px;width:240px"><h4>Newsletter Subscribe</h4>
    <p style="margin-top:14px">We will inform you about newest project and promotions.Subscribe to our newsletter.</p>
    <div class="signup"><span>Your Email Address</span><b><svg width="12" height="12"><path d="M2 6h8M6 2l4 4-4 4" stroke="#fff" stroke-width="2" fill="none"/></svg></b></div>
  </div>
</footer>
<div class="bottombar">
  <div class="copy">© Copyright 2017 BROVINACORP. All Rights Reserved.</div>
  <div class="social"><span class="dot-icon"></span><span class="dot-icon"></span><span class="dot-icon"></span><span class="dot-icon"></span><span class="dot-icon"></span></div>
</div>

</body>
</html>
```